RepMeadow.com "RE-SKIN" project

We have an existing site that we've recently built that needs to be re-formatted, skinned and polished. Our current developer did an amazing job building the backend but it not an expert in design and formatting of HTML and Web design. We need to have site cleaned up with all new formatting, layout, design elements and visual effects. ALl the date and functionality of the site will remain the same.

We would like to see Home page mock ups that may include Photo's, Flash, etc. or any other design element the designer feels would convey, a corporate, business oriented, simple and clean feel. The way the site currently looks is very basic and we need to have a slick, visual pleasing and easy to navigate design to go with our new functionality. The home page design will then need to translate over into the remaining pages of the site.

This is business to business site and will act as recruitment tool for medical device organizations. We have created a nationwide database of the top medical distributor groups (independent sale reps and groups). We act a "dating site" for medical manufacturers to find the best reps to sell their products.

NOTES on DESIGN:

* THE FUNCTION AND DATA OF THE SITE WILL REMAIN THE SAME, THIS PROJECT WILL BE TAKING ALL EXISTING INFO AND RE-DESIGNING THE LAYOUT.

*Must keep same color scheme

*Home Page design will be main focus and then ALL other pages need to follow style and template of Home page

* The sign up process on the site is in desperate need of re-design and we would like to see BIG, Step by Step, windows that make it feel very simple for the user to fill out (Best example we can think of is the Wellcover.gov site step by step sign up process. As bad as the overall functionality is on that site, the sign up process and drop down menu steps are easy to fill out.)

*The site is currently in a very basic "utilitarian" style and has very little in way of design, text formatting, and overall appearance. We need to have the designer go through each page and JUSTIFY, RE-SIZE, RE-SCALE and dress up all the current information displayed.

* We need the display pages to be easier to read, have better flow and more visually pleasing. (EXAMPLE: ANy search results that are done on the site come back in very table driven, hard to read, small text with small logo. We would like to see more design elements with updated formats and hopefully larger icons and east to read and navigate text

* WE ARE OPEN TO ANY DESIGN IDEAS OR MOCK UPS.

* Logos, icons, animation etc need to remain the same.

*Home page can feature video or photos but the remainder of the site will remian data only.
Updates

We would suggest doing a Mock up of the HOME PAGE only to begin with. We can then evaluate and choose a design theme/concept to carry over into the remainder of the pages.

Target Market(s)

Independent Medical Sales Distributors (sales reps) and Medical device manufacturers.

Industry/Entity Type

Recruitment

Coding

Coded - Design and coding required

Number of Pages Required

5+ page

Font styles to use
Sans Serif

Colors
0492cd
0455a3
3176b5
cedeed
85cae6
fcfdfe

Requirements
Must have
• *Must be Mobile Friendly
• *Must use all the info, links, logos and icons currently on www.RepMeadow.com
• *All pages of the site must follow to layout and design of the Home Page that is created in this project
• *Every page needs to be updated
Nice to have
• Glossy, crisp home page, that incorporate "stock" photos or animation for a more promotional or brochure type of feel
• Easy to navigate, bigger text and buttons and icons.
Should not have
• Color scheme and logo should not change

```html
<!DOCTYPE html>
<html lang="en">
<head>
<meta charset="utf-8">
<title>RepMeadow.com</title>
<link href="https://fonts.googleapis.com/css2?family=Lato:wght@400;700;900&family=Catamaran:wght@700;800&family=Encode+Sans+Condensed:wght@400;700&display=swap" rel="stylesheet">
<style>
:root{
  --blue:#0455a3;
  --blue-mid:#1b62b0;
  --green:#78c03a;
  --ink:#333;
  --muted:#555;
  --line:#c9c9c9;
  --footer:#000;
  --white:#fff;
}
*{box-sizing:border-box;margin:0;padding:0}
html,body{width:930px;height:1200px;overflow:hidden;background:var(--white)}
body{position:relative;font-family:Lato,sans-serif;color:var(--ink)}
.abs{position:absolute}
.site-header{position:absolute;left:0;top:0;width:930px;height:72px;border-bottom:2px solid #ddd;box-shadow:0 1px 2px rgba(0,0,0,.08)}
.brand{position:absolute;left:76px;top:20px;display:flex;align-items:center;gap:8px;font-family:Lato,sans-serif;font-weight:900;font-size:22px;color:#111}
.brand-mark{width:28px;height:28px;background:var(--blue);border-radius:4px}
.main-nav{position:absolute;top:28px;left:322px;display:flex;gap:22px;font-size:12.5px;font-weight:700;color:#333}
.main-nav .active{color:var(--green)}
.search-icon{position:absolute;left:736px;top:28px}
.login-btn{position:absolute;left:774px;top:17px;width:78px;height:35px;border:2px solid var(--green);border-radius:18px;color:var(--green);font-weight:900;font-size:13px;display:flex;align-items:center;justify-content:center;gap:4px}
.breadcrumb{position:absolute;left:76px;top:103px;font-size:12px;font-weight:700;color:#333}
.breadcrumb .current{color:var(--blue-mid)}
.rule{position:absolute;left:76px;width:778px;height:1px;background:#bbb}
.headline{position:absolute;left:60px;top:196px;width:810px;text-align:center;font-family:Catamaran,sans-serif;font-weight:800;font-size:28px;line-height:40px;color:var(--blue-mid)}
.search-bar .select{position:absolute;top:354px;height:36px;border:1px solid #bbb;font-size:12px;color:#555;padding-left:11px;line-height:34px}
.select::after{content:"";position:absolute;right:0;top:0;width:38px;height:34px;border-left:1px solid #bbb}
.select .caret{position:absolute;right:15px;top:15px;border:4px solid transparent;border-top:5px solid #444;z-index:1}
.search-btn{position:absolute;left:735px;top:352px;width:118px;height:39px;border-radius:20px;background:var(--green);color:#fff;font-weight:900;font-size:15px;display:flex;align-items:center;justify-content:center}
.card{position:absolute;top:510px;width:364px;height:321px;border:2px solid;border-radius:3px;text-align:center}
.card.dist{left:77px;border-color:var(--blue-mid)}
.card.lines{left:490px;border-color:var(--green)}
.card-icon{position:absolute;left:141px;top:-45px;width:80px;height:80px;border-radius:50%;box-shadow:3px 3px 0 #fff,4px 4px 6px rgba(0,0,0,.25);outline:6px solid #fff}
.dist .card-icon{background:var(--blue-mid)}
.lines .card-icon{background:var(--green)}
.card h2{position:absolute;top:54px;width:100%;font-family:"Encode Sans Condensed",sans-serif;font-weight:700;font-size:19px}
.dist h2{color:var(--blue-mid)}
.lines h2{color:var(--green)}
.card p{position:absolute;top:89px;left:50px;width:260px;font-family:"Encode Sans Condensed",sans-serif;font-size:13px;line-height:17px;color:#333}
.field{position:absolute;left:30px;width:302px;height:37px;border:1px solid #aaa;font-size:12px;color:#555;text-align:left;padding-left:24px;line-height:35px}
.field svg{position:absolute;left:10px;top:12px}
.card .btn{position:absolute;left:126px;top:254px;width:112px;height:40px;border-radius:20px;color:#fff;font-weight:900;font-size:12.5px;line-height:40px}
.dist .btn{background:var(--blue-mid)}
.lines .btn{background:var(--green)}
.site-footer{position:absolute;left:0;top:913px;width:930px;height:287px;background:var(--footer);color:#fff}
.foot-brand{position:absolute;left:79px;top:95px;display:flex;align-items:center;gap:7px;font-weight:900;font-size:20px}
.foot-brand span{width:26px;height:26px;background:#fff;border-radius:4px}
.social{position:absolute;top:148px;width:25px;height:25px;border:1px solid #ccc;border-radius:50%}
.site-footer h3{position:absolute;top:57px;font-size:14px;font-weight:700}
.quick a{display:block;color:#fff;text-decoration:none;font-size:10px;line-height:19.2px}
.small{font-size:10px;line-height:16px}
.email-in{position:absolute;left:447px;top:131px;width:197px;height:27px;background:#fff;color:#666;font-size:9.5px;padding-left:10px;line-height:27px}
.sub-btn{position:absolute;left:446px;top:170px;width:84px;height:30px;background:var(--green);border-radius:15px;font-size:10px;font-weight:700;line-height:30px;text-align:center}
.contact-row{position:absolute;left:698px;font-size:9.5px;line-height:16px}
.contact-row svg{position:absolute;left:0;top:2px}
.contact-row div{margin-left:27px}
.foot-rule{position:absolute;left:76px;top:222px;width:778px;height:1px;background:#444}
.copy{position:absolute;top:246px;width:930px;text-align:center;font-size:10px}
</style>
</head>
<body>
<header class="site-header">
  <div class="brand"><span class="brand-mark"></span>RepMeadow.com</div>
  <nav class="main-nav"><span>HOW IT WORKS</span><span>SIGNUP</span><span>PRODUCTS</span><span class="active">SEARCH</span><span>RESOURCES</span></nav>
  <svg class="search-icon" width="13" height="13" viewBox="0 0 13 13"><circle cx="5.5" cy="5.5" r="4" fill="none" stroke="#333" stroke-width="2"/><line x1="8.5" y1="8.5" x2="12" y2="12" stroke="#333" stroke-width="2.2"/></svg>
  <div class="login-btn"><svg width="9" height="11" viewBox="0 0 9 11"><path d="M2 5V3.5a2.5 2.5 0 0 1 5 0V5" fill="none" stroke="#78c03a" stroke-width="1.5"/><rect x="0.5" y="5" width="8" height="6" rx="1" fill="#78c03a"/></svg>LOGIN</div>
</header>

<div class="breadcrumb">HOME &nbsp;&gt;&gt;&nbsp; SEARCH &nbsp;&gt;&gt;&nbsp; <span class="current">DISTRIBUTORS PROFILE</span></div>
<div class="rule" style="top:136px"></div>

<h1 class="headline">THE WEB'S FASTEST GROWING RESOURCE FOR INDEPENDENT MEDICAL SALES WE MATCH DISTRIBUTORS WITH TOP PROSPECT LINES!</h1>

<div class="search-bar">
  <div class="select" style="left:76px;width:152px">Search For<span class="caret"></span></div>
  <div class="select" style="left:236px;width:238px">Select States<span class="caret"></span></div>
  <div class="select" style="left:482px;width:238px">Select States<span class="caret"></span></div>
  <div class="search-btn">SEARCH</div>
</div>

<section class="card dist">
  <div class="card-icon" role="img" aria-label="Megaphone icon"></div>
  <h2>I NEED DISTRIBUTORS</h2>
  <p>Find top medical distributor reps or groups to sell your product.</p>
  <div class="field" style="top:150px"><svg width="9" height="10" viewBox="0 0 9 10"><circle cx="4.5" cy="2.7" r="2.5" fill="#555"/><path d="M0 10c0-3.5 2-5 4.5-5S9 6.5 9 10z" fill="#555"/></svg>User ID</div>
  <div class="field" style="top:197px"><svg width="8" height="10" viewBox="0 0 8 10"><path d="M1.8 4.5V3a2.2 2.2 0 0 1 4.4 0v1.5" fill="none" stroke="#555" stroke-width="1.3"/><rect y="4.5" width="8" height="5.5" fill="#555"/></svg>Password</div>
  <div class="btn">SIGNUP NOW</div>
</section>

<section class="card lines">
  <div class="card-icon" role="img" aria-label="Briefcase icon"></div>
  <h2>I NEED NEW PRODUCT LINES</h2>
  <p>Locate and secure the top available medical product lines in your area.</p>
  <div class="field" style="top:150px"><svg width="9" height="10" viewBox="0 0 9 10"><circle cx="4.5" cy="2.7" r="2.5" fill="#555"/><path d="M0 10c0-3.5 2-5 4.5-5S9 6.5 9 10z" fill="#555"/></svg>User ID</div>
  <div class="field" style="top:197px"><svg width="8" height="10" viewBox="0 0 8 10"><path d="M1.8 4.5V3a2.2 2.2 0 0 1 4.4 0v1.5" fill="none" stroke="#555" stroke-width="1.3"/><rect y="4.5" width="8" height="5.5" fill="#555"/></svg>Password</div>
  <div class="btn">SIGNUP NOW</div>
</section>

<footer class="site-footer">
  <div class="foot-brand"><span></span>RepMeadow.com</div>
  <div class="social" style="left:116px"></div>
  <div class="social" style="left:147px"></div>
  <div class="social" style="left:178px"></div>
  <div class="social" style="left:209px"></div>

  <h3 style="left:311px">QUICK LINKS</h3>
  <nav class="quick abs" style="left:311px;top:86px"><a>Help</a><a>FAQ</a><a>Support</a><a>Sitemap</a><a>Terms Of Use</a><a>Privacy Statement</a></nav>

  <h3 style="left:447px">NEWSLETTER SUBSCRIPTION</h3>
  <div class="small abs" style="left:447px;top:92px;width:170px">Register your Email Address to get Information about us</div>
  <div class="email-in">Email Address</div>
  <div class="sub-btn">SUBSCRIBE</div>

  <h3 style="left:698px">CONTACT US</h3>
  <div class="contact-row" style="top:89px"><svg width="8" height="11" viewBox="0 0 8 11"><path d="M4 11S0 6 0 4a4 4 0 0 1 8 0c0 2-4 7-4 7z" fill="#fff"/><circle cx="4" cy="4" r="1.5" fill="#000"/></svg><div>1180 NW CEDAR MILL RD<br>SUITE #210 BEAVERTON, OR 97006</div></div>
  <div class="contact-row" style="top:137px"><svg width="10" height="10" viewBox="0 0 10 10"><path d="M2 0l2 2.5-1.2 1.2a6 6 0 0 0 3.5 3.5L7.5 6 10 8l-1.5 2C4 10 0 6 0 1.5z" fill="#fff"/></svg><div>1 800 555 0142</div></div>
  <div class="contact-row" style="top:169px"><svg width="12" height="9" viewBox="0 0 12 9"><rect width="12" height="9" fill="#fff"/><path d="M0 0l6 5 6-5" fill="none" stroke="#000" stroke-width="1"/></svg><div>info@repmeadow.com</div></div>

  <div class="foot-rule"></div>
  <div class="copy">Copyrights © 2018, RepMeadow. All rights reserved.</div>
</footer>
</body>
</html>
```